LatAm Power Generation PPT - Corporate office in Houston, TX - USA

Here's our website: norvalepower.example. We are Norvale Power Management LLC. We are a small corporate office that manages power generation assets located in Latin America. We are pro clean energy, including thermal generation as long as it is gas-fired equipment (no coal-fired plants in our portfolio). Brazil is the first country where we have a presence in and we intend to grow significantly in the region in the next few years. We report to a private equity in the US, that is a co-investor. We would like a formal, elegant and detailed presentation for Board meetings, Budget reviews, Investment proposals, etc.
We have a logo/business cards just created with a CraftHive designer, which are uploaded.
Updates

Everyone: Focus of our core business is conventional energy, primarily thermal energy (except Coal). All the same, renewable energy is relevant, just not the sole objective. Thanks for participating!

```html
<!DOCTYPE html>
<html lang="en">
<head>
<meta charset="utf-8">
<title>Norvale Power – Board Deck Template</title>
<link href="https://fonts.googleapis.com/css2?family=Open+Sans:wght@400;600;700;800&display=swap" rel="stylesheet">
<style>
:root{
  --green:#1fa21f;
  --green-lt:#3cc13c;
  --navy:#1b2b70;
  --blue:#2456b8;
  --gray:#9a9a9a;
  --gray-lt:#e6e6e6;
  --ink:#222;
  --text:#555;
  --canvas:#c9c9c9;
}
*{box-sizing:border-box;margin:0;padding:0}
html,body{width:794px;height:1200px;overflow:hidden}
body{background:var(--canvas);font-family:"Open Sans",Arial,sans-serif;color:var(--ink);position:relative}
.slide{position:absolute;width:257px;height:145px;background:#fff;overflow:hidden}
.abs{position:absolute}
.photo{position:absolute}
.title{position:absolute;top:15px;left:0;width:100%;text-align:center;font-weight:800;font-size:7.4px;letter-spacing:.2px;color:var(--ink)}
.brand{position:absolute;top:5px;right:6px;font-weight:800;font-size:4px;color:var(--green);display:flex;align-items:center;gap:2px}
.brand i{display:block;width:5px;height:5px;border-radius:50%;background:var(--green)}
.wave{position:absolute;left:0;bottom:0;width:257px;height:14px}
.tx{font-size:2.6px;line-height:3.4px;color:var(--text)}
.tx-w{font-size:2.6px;line-height:3.4px;color:#fff}
.hd{font-weight:700;font-size:3.4px}
.num-g{color:var(--green);font-weight:800}
table{border-collapse:collapse}
.tbl td{font-size:2.5px;padding:0 2px;height:7.4px;color:var(--text)}
.tbl tr:nth-child(odd) td{background:#f0f0f0}
.tbl th{font-size:2.4px;color:#fff;height:10px;font-weight:700}
.circ{border-radius:50%}
.tick{display:flex;gap:3px;align-items:flex-start;margin-bottom:4px}
.tick span.c{flex:none;width:6px;height:6px;border-radius:50%;background:#fff;position:relative}
.tick span.c::after{content:"";position:absolute;left:1.6px;top:1.2px;width:2.4px;height:1.4px;border-left:1px solid var(--blue);border-bottom:1px solid var(--blue);transform:rotate(-45deg)}
</style>
</head>
<body>

<svg width="0" height="0" style="position:absolute">
  <defs>
    <symbol id="wave" viewBox="0 0 257 14">
      <path d="M0 5 C60 -1 130 12 257 1 L257 14 L0 14Z" fill="#1fa21f"/>
      <path d="M0 9 C80 4 160 15 257 6 L257 14 L0 14Z" fill="#1b2b70"/>
    </symbol>
  </defs>
</svg>

<!-- 1 Cover -->
<section class="slide" style="left:9px;top:8px">
  <div class="photo" role="img" aria-label="Transmission towers at a power substation at dusk" style="inset:0;background:linear-gradient(180deg,#7d8a8f 0%,#6d7a6a 55%,#556b3a 100%)"></div>
  <div class="abs" style="left:52px;top:55px;width:6px;height:46px;border:2px solid var(--green);border-right:none;border-radius:4px 0 0 4px"></div>
  <div class="abs" style="right:52px;top:55px;width:6px;height:46px;border:2px solid var(--green);border-left:none;border-radius:0 4px 4px 0"></div>
  <div class="abs" style="left:0;width:100%;top:34px;text-align:center;font-weight:800;font-size:9px;color:#fff"><i style="display:inline-block;width:7px;height:7px;border-radius:50%;background:#fff;margin-right:2px"></i>NORVALE Power</div>
  <div class="abs" style="left:0;width:100%;top:69px;text-align:center;font-weight:700;font-size:11px;color:#fff">Your Slides Deck Name</div>
  <div class="abs" style="left:0;width:100%;top:84px;text-align:center;font-size:5px;color:#eee">Your Slides Deck Name</div>
</section>

<!-- 2 Brand slide -->
<section class="slide" style="left:270px;top:8px">
  <div class="photo" role="img" aria-label="Pylon, wind turbines and solar panels under a sunset sky" style="inset:0;background:linear-gradient(180deg,#8fa4b6 0%,#d8c8a8 55%,#5b6a78 100%)"></div>
  <svg class="abs" style="left:0;top:0" width="257" height="145" viewBox="0 0 257 145">
    <path d="M0 0 L30 0 L0 120Z" fill="#1b2b70"/>
    <path d="M0 0 L18 0 L0 80Z" fill="#1fa21f"/>
    <path d="M257 145 L120 145 L257 115Z" fill="#1fa21f"/>
    <path d="M257 145 L160 145 L257 128Z" fill="#1b2b70"/>
  </svg>
  <div class="abs" style="left:0;width:100%;top:64px;text-align:center;font-weight:800;font-size:12px;color:var(--green)"><i style="display:inline-block;width:10px;height:10px;border-radius:50%;background:var(--green);margin-right:3px;vertical-align:-1px"></i>NORVALE Power</div>
</section>

<!-- 3 Section divider -->
<section class="slide" style="left:530px;top:8px">
  <div class="photo" role="img" aria-label="Wind turbines on a grassy plain under a bright sky" style="inset:0;background:linear-gradient(180deg,#c6d6e6 0%,#eef2f5 60%,#7c9a4a 85%,#5d7a34 100%)"></div>
  <div class="abs" style="left:0;top:52px;width:136px;height:40px;background:rgba(255,255,255,.92)"></div>
  <div class="abs" style="left:72px;top:63px;font-weight:800;font-size:8.5px;line-height:10px;color:var(--ink);text-align:right">BUSINESS<br>OVERVIEW</div>
  <div class="abs" style="left:130px;top:52px;width:28px;height:40px;background:var(--green);color:#fff;font-weight:800;font-size:16px;display:flex;align-items:center;justify-content:center">01</div>
</section>

<!-- 4 Energy sources -->
<section class="slide" style="left:9px;top:157px">
  <div class="brand"><i></i>NORVALE</div>
  <div class="title">YOUR TITLE GOES HERE</div>
  <div class="abs" style="left:10px;top:30px;display:flex;gap:3px">
    <div style="width:57px;height:98px;background:var(--green);padding:3px;text-align:center">
      <div class="tx-w" style="font-weight:700">ENERGY SOURCES<br>01</div>
      <div class="tx-w" style="margin-top:3px">Lorem ipsum dolor sit amet, consectetur adipiscing elit sed do eiusmod tempor labore et dolore magna aliqua enim.</div>
      <div class="circ" style="width:16px;height:16px;background:#fff;margin:10px auto 0"></div>
    </div>
    <div style="width:57px;height:98px;background:var(--gray);padding:3px;text-align:center">
      <div class="tx-w" style="font-weight:700">ENERGY SOURCES<br>02</div>
      <div class="tx-w" style="margin-top:3px">Lorem ipsum dolor sit amet, consectetur adipiscing elit sed do eiusmod tempor labore et dolore magna aliqua enim.</div>
      <div style="width:12px;height:16px;border:1.5px solid #fff;border-radius:2px;margin:10px auto 0"></div>
    </div>
    <div style="width:57px;height:98px;background:var(--green);padding:3px;text-align:center">
      <div class="tx-w" style="font-weight:700">ENERGY SOURCES<br>03</div>
      <div class="tx-w" style="margin-top:3px">Lorem ipsum dolor sit amet, consectetur adipiscing elit sed do eiusmod tempor labore et dolore magna aliqua enim.</div>
      <div style="width:2px;height:16px;background:#fff;margin:10px auto 0"></div>
    </div>
    <div style="width:57px;height:98px;background:var(--gray);padding:3px;text-align:center">
      <div class="tx-w" style="font-weight:700">ENERGY SOURCES<br>04</div>
      <div class="tx-w" style="margin-top:3px">Lorem ipsum dolor sit amet, consectetur adipiscing elit sed do eiusmod tempor labore et dolore magna aliqua enim.</div>
      <div style="width:16px;height:10px;background:#fff;margin:13px auto 0;transform:skewX(-15deg)"></div>
    </div>
  </div>
  <svg class="wave"><use href="#wave"/></svg>
</section>

<!-- 5 Agenda -->
<section class="slide" style="left:270px;top:157px">
  <div class="brand"><i></i>NORVALE</div>
  <div class="abs" style="left:41px;top:67px;font-weight:600;font-size:11.5px">Agenda</div>
  <div class="abs" style="left:128px;top:0;width:14px;height:145px;background:var(--green)"></div>
  <div class="abs" style="left:128px;top:22px;width:120px">
    <div style="display:flex;gap:3px;height:23px;align-items:flex-start"><span style="width:14px;text-align:center;background:#fff;color:var(--navy);font-weight:800;font-size:7px">01</span><div><div class="hd">Contents</div><div class="tx">Get a modern PowerPoint Presentation that is beautifully designed.</div></div></div>
    <div style="display:flex;gap:3px;height:23px;align-items:flex-start"><span style="width:14px;text-align:center;background:#fff;color:var(--navy);font-weight:800;font-size:7px">02</span><div><div class="hd">Contents</div><div class="tx">Get a modern PowerPoint Presentation that is beautifully designed.</div></div></div>
    <div style="display:flex;gap:3px;height:23px;align-items:flex-start"><span style="width:14px;text-align:center;background:#fff;color:var(--navy);font-weight:800;font-size:7px">03</span><div><div class="hd">Contents</div><div class="tx">Get a modern PowerPoint Presentation that is beautifully designed.</div></div></div>
    <div style="display:flex;gap:3px;height:23px;align-items:flex-start"><span style="width:14px;text-align:center;background:#fff;color:var(--navy);font-weight:800;font-size:7px">04</span><div><div class="hd">Contents</div><div class="tx">Get a modern PowerPoint Presentation that is beautifully designed.</div></div></div>
    <div style="display:flex;gap:3px;height:23px;align-items:flex-start"><span style="width:14px;text-align:center;background:#fff;color:var(--navy);font-weight:800;font-size:7px">05</span><div><div class="hd">Contents</div><div class="tx">Get a modern PowerPoint Presentation that is beautifully designed.</div></div></div>
  </div>
  <svg class="wave"><use href="#wave"/></svg>
</section>

<!-- 6 Photo with cards -->
<section class="slide" style="left:530px;top:157px">
  <div class="photo" role="img" aria-label="Solar farm with wind turbines under blue sky" style="inset:0;background:linear-gradient(180deg,#3f6fb0 0%,#8aa9cf 45%,#6c7f95 100%)"></div>
  <div class="title" style="color:#fff">YOUR TITLE GOES HERE</div>
  <div class="tx-w abs" style="left:40px;top:50px;width:180px;text-align:center">Lorem ipsum dolor sit amet, consectetur adipiscing elit, sed do eiusmod tempor incididunt ut labore et dolore magna aliqua sed do eiusmod.</div>
  <div class="abs" style="left:10px;top:70px;display:flex;gap:10px">
    <div class="tx" style="width:75px;height:58px;background:#fff;border-radius:5px;padding:4px">Lorem ipsum dolor sit amet, consectetur adipiscing elit, sed do eiusmod tempor incididunt ut labore et dolore magna aliqua sed do eiusmod tempor.</div>
    <div class="tx" style="width:75px;height:58px;background:#fff;border-radius:5px;padding:4px">Lorem ipsum dolor sit amet, consectetur adipiscing elit, sed do eiusmod tempor incididunt ut labore et dolore magna aliqua sed do eiusmod tempor.</div>
    <div class="tx" style="width:75px;height:58px;background:#fff;border-radius:5px;padding:4px">Lorem ipsum dolor sit amet, consectetur adipiscing elit, sed do eiusmod tempor incididunt ut labore et dolore magna aliqua sed do eiusmod tempor.</div>
  </div>
  <div class="abs circ" style="left:80px;top:94px;width:11px;height:11px;background:var(--green);color:#fff;font-size:7px;text-align:center;line-height:10px">›</div>
  <div class="abs circ" style="left:165px;top:94px;width:11px;height:11px;background:var(--green);color:#fff;font-size:7px;text-align:center;line-height:10px">›</div>
</section>

<!-- 7 Two-column text -->
<section class="slide" style="left:9px;top:306px">
  <div class="brand"><i></i>NORVALE</div>
  <div class="title">YOUR TITLE GOES HERE</div>
  <div class="tx abs" style="left:16px;top:36px;width:100px">Lorem ipsum dolor sit amet, consectetur adipiscing elit, sed do eiusmod tempor incididunt ut labore et dolore magna aliqua. Ut enim ad minim veniam, quis nostrud exercitation ullamco laboris nisi ut aliquip ex ea commodo consequat duis aute irure dolor in reprehenderit.</div>
  <div class="tx abs" style="left:138px;top:36px;width:100px">Lorem ipsum dolor sit amet, consectetur adipiscing elit, sed do eiusmod tempor incididunt ut labore et dolore magna aliqua. Ut enim ad minim veniam, quis nostrud exercitation ullamco laboris nisi ut aliquip ex ea commodo consequat duis aute irure dolor in reprehenderit.</div>
  <div class="abs" style="left:16px;top:91px;width:100px">
    <div class="tx" style="display:flex;gap:4px;margin-bottom:8px"><span style="color:var(--navy);font-size:5px">▶</span>Lorem ipsum dolor sit amet, consectetur adipiscing elit.</div>
    <div class="tx" style="display:flex;gap:4px"><span style="color:var(--green);font-size:5px">▶</span>Lorem ipsum dolor sit amet, consectetur adipiscing elit.</div>
  </div>
  <div class="abs" style="left:138px;top:91px;width:100px">
    <div class="tx" style="display:flex;gap:4px;margin-bottom:8px"><span style="color:var(--navy);font-size:5px">▶</span>Lorem ipsum dolor sit amet, consectetur adipiscing elit.</div>
    <div class="tx" style="display:flex;gap:4px"><span style="color:var(--green);font-size:5px">▶</span>Lorem ipsum dolor sit amet, consectetur adipiscing elit.</div>
  </div>
  <svg class="wave"><use href="#wave"/></svg>
</section>

<!-- 8 Data table -->
<section class="slide" style="left:270px;top:306px">
  <div class="brand"><i></i>NORVALE</div>
  <div class="title">YOUR TITLE GOES HERE</div>
  <table class="tbl abs" style="left:14px;top:36px;width:230px;text-align:center">
    <tr><th style="background:#fff"></th><th style="background:var(--navy)">Lorem ipsum</th><th style="background:var(--green)">Lorem ipsum</th><th style="background:var(--navy)">Lorem ipsum</th><th style="background:var(--green)">Lorem ipsum</th><th style="background:var(--navy)">Lorem ipsum</th></tr>
    <tr><td style="text-align:left">Lorem ipsum dolor</td><td>23</td><td>45</td><td>4</td><td>4</td><td>34</td></tr>
    <tr><td style="text-align:left">Lorem ipsum dolor</td><td>234</td><td>75</td><td>4</td><td>4</td><td>66</td></tr>
    <tr><td style="text-align:left">Lorem ipsum dolor</td><td>55</td><td>75</td><td>64</td><td>6</td><td>44</td></tr>
    <tr><td style="text-align:left">Lorem ipsum dolor</td><td>66</td><td>45</td><td>4</td><td>4</td><td>44</td></tr>
    <tr><td style="text-align:left">Lorem ipsum dolor</td><td>78</td><td>64</td><td>46</td><td>6</td><td>34</td></tr>
    <tr><td style="text-align:left">Lorem ipsum dolor</td><td>56</td><td>46</td><td>44</td><td>3</td><td>55</td></tr>
  </table>
  <svg class="wave"><use href="#wave"/></svg>
</section>

<!-- 9 Photo + ticks -->
<section class="slide" style="left:530px;top:306px">
  <div class="brand"><i></i>NORVALE</div>
  <div class="title">YOUR TITLE GOES HERE</div>
  <div class="photo" role="img" aria-label="Aerial view of a solar panel field beside green land" style="left:0;top:34px;width:100px;height:104px;background:linear-gradient(135deg,#2d4f8f 0%,#3e6aa8 55%,#5f8a3a 100%)"></div>
  <div class="abs" style="left:92px;top:34px;width:165px;height:104px;background:var(--navy);padding:8px 6px;display:grid;grid-template-columns:1fr 1fr;column-gap:6px">
    <div class="tick"><span class="c"></span><div class="tx-w"><b>Lorem ipsum dolor</b><br>Lorem ipsum dolor sit amet consectetur</div></div>
    <div class="tick"><span class="c"></span><div class="tx-w"><b>Lorem ipsum dolor</b><br>Lorem ipsum dolor sit amet consectetur</div></div>
    <div class="tick"><span class="c"></span><div class="tx-w"><b>Lorem ipsum dolor</b><br>Lorem ipsum dolor sit amet consectetur</div></div>
    <div class="tick"><span class="c"></span><div class="tx-w"><b>Lorem ipsum dolor</b><br>Lorem ipsum dolor sit amet consectetur</div></div>
    <div class="tick"><span class="c"></span><div class="tx-w"><b>Lorem ipsum dolor</b><br>Lorem ipsum dolor sit amet consectetur</div></div>
    <div class="tick"><span class="c"></span><div class="tx-w"><b>Lorem ipsum dolor</b><br>Lorem ipsum dolor sit amet consectetur</div></div>
  </div>
  <svg class="wave"><use href="#wave"/></svg>
</section>

<!-- 10 Lists -->
<section class="slide" style="left:9px;top:454px">
  <div class="brand"><i></i>NORVALE</div>
  <div class="abs" style="left:12px;top:64px;width:100px;text-align:center;font-weight:700;font-size:8.5px;line-height:10px">Sed ut perspiciatis unde</div>
  <div class="abs" style="left:114px;top:12px;width:124px">
    <div class="tx-w" style="background:var(--navy);padding:1px 3px;font-weight:700">Get a modern PowerPoint</div>
    <div class="tx" style="padding:2px 3px 6px">• Get a modern PowerPoint presentation<br>• Easy to change colors, photos and text<br>• This text can be replaced with your own<br>• I hope and I believe this template will save time</div>
    <div class="tx-w" style="background:var(--green);padding:1px 3px;font-weight:700">Get a modern PowerPoint</div>
    <div class="tx" style="padding:2px 3px 6px">• Get a modern PowerPoint presentation<br>• Easy to change colors, photos and text<br>• This text can be replaced with your own<br>• I hope and I believe this template will save time</div>
    <div class="tx-w" style="background:var(--gray);padding:1px 3px;font-weight:700">Get a modern PowerPoint</div>
    <div class="tx" style="padding:2px 3px">• Get a modern PowerPoint presentation<br>• Easy to change colors, photos and text<br>• This text can be replaced with your own<br>• I hope and I believe this template will save time</div>
  </div>
  <svg class="wave"><use href="#wave"/></svg>
</section>

<!-- 11 Map -->
<section class="slide" style="left:270px;top:454px">
  <div class="brand"><i></i>NORVALE</div>
  <div class="title">YOUR TITLE GOES HERE</div>
  <div class="photo" role="img" aria-label="World map with highlighted locations in Latin America and Asia" style="left:34px;top:30px;width:190px;height:98px;background:radial-gradient(ellipse at 50% 45%,#9c9c9c 0%,#b5b5b5 55%,#fff 75%)"></div>
  <div class="abs circ" style="left:95px;top:96px;width:8px;height:8px;background:var(--green);opacity:.8"></div>
  <div class="abs circ" style="left:185px;top:74px;width:8px;height:8px;background:var(--green);opacity:.8"></div>
  <svg class="wave"><use href="#wave"/></svg>
</section>

<!-- 12 Financials -->
<section class="slide" style="left:530px;top:454px">
  <div class="brand"><i></i>NORVALE</div>
  <div class="title">YOUR TITLE GOES HERE</div>
  <table class="abs" style="left:36px;top:30px;width:210px;font-size:2.6px;text-align:center;color:var(--text)">
    <tr style="height:5px"><td></td><td></td><td style="background:var(--blue);color:#fff">2019</td><td style="background:var(--blue);color:#fff">2020</td><td style="background:var(--blue);color:#fff">2021</td><td style="background:var(--blue);color:#fff">2022</td></tr>
    <tr style="height:4px"><td style="text-align:left;font-weight:700">Revenue</td><td></td><td></td><td></td><td></td><td></td></tr>
    <tr style="height:4px"><td style="text-align:left;background:var(--gray);color:#fff">Licence fees</td><td>£</td><td>1,787,100</td><td>6,177,000</td><td>10,807,000</td><td>12,580,000</td></tr>
    <tr style="height:4px"><td style="text-align:left;background:var(--gray);color:#fff">Revenue share</td><td>£</td><td>630,000</td><td>11,474,750</td><td>15,414,000</td><td>15,414,000</td></tr>
    <tr style="height:4px"><td style="text-align:left;background:var(--gray);color:#fff">Development fee</td><td>£</td><td>100,000</td><td>200,000</td><td>200,000</td><td>200,000</td></tr>
    <tr style="height:4px;background:var(--green);color:#fff"><td style="text-align:left">Total Revenue</td><td>£</td><td>2,517,100</td><td>17,851,750</td><td>26,421,000</td><td>28,194,000</td></tr>
    <tr style="height:10px"><td colspan="6"></td></tr>
    <tr style="height:5px;background:var(--green);color:#fff"><td style="text-align:left">Operating costs</td><td>£</td><td>1,408,910</td><td>2,522,838</td><td>2,852,835</td><td>2,978,111</td></tr>
    <tr style="height:10px"><td colspan="6"></td></tr>
    <tr style="height:5px;background:var(--green);color:#fff"><td style="text-align:left">Operating profit</td><td>£</td><td>1,108,190</td><td>15,328,912</td><td>23,568,165</td><td>25,215,887</td></tr>
    <tr style="height:10px"><td colspan="6"></td></tr>
    <tr style="height:5px;background:var(--blue);color:#fff"><td style="text-align:left">Net profit</td><td>£</td><td>887,654</td><td>12,569,708</td><td>18,325,895</td><td>20,928,356</td></tr>
  </table>
  <svg class="wave"><use href="#wave"/></svg>
</section>

<!-- 13 Photo panel -->
<section class="slide" style="left:9px;top:603px">
  <div class="photo" role="img" aria-label="Wind turbines on a field under a cloudy sky" style="inset:0;background:linear-gradient(180deg,#4d6a86 0%,#b8c6d2 50%,#6f8a4a 100%)"></div>
  <div class="abs" style="left:16px;top:12px;width:225px;height:128px;background:rgba(255,255,255,.78)"></div>
  <div class="title" style="top:26px">YOUR TITLE GOES HERE</div>
  <div class="abs" style="left:65px;top:48px;width:2px;height:18px;background:var(--navy)"></div>
  <div class="abs" style="left:59px;top:50px;width:14px;height:3px;background:var(--navy);transform:rotate(-20deg)"></div>
  <div class="abs" style="left:178px;top:52px;width:16px;height:11px;background:var(--navy);transform:skewX(-15deg)"></div>
  <div class="tx abs" style="left:24px;top:78px;width:100px">Lorem ipsum dolor sit amet, consectetur adipiscing elit, sed do eiusmod tempor incididunt ut labore et dolore magna aliqua. Ut enim ad minim veniam, quis nostrud exercitation ullamco laboris nisi ut aliquip ex ea commodo consequat.</div>
  <div class="tx abs" style="left:134px;top:78px;width:100px">Lorem ipsum dolor sit amet, consectetur adipiscing elit, sed do eiusmod tempor incididunt ut labore et dolore magna aliqua. Ut enim ad minim veniam, quis nostrud exercitation ullamco laboris nisi ut aliquip ex ea commodo consequat.</div>
</section>

<!-- 14 Text over photo -->
<section class="slide" style="left:270px;top:603px">
  <div class="brand"><i></i>NORVALE</div>
  <div class="photo" role="img" aria-label="Wind turbines and solar panels beside green fields" style="left:0;top:0;width:150px;height:145px;background:linear-gradient(160deg,#7ea2c9 0%,#c5d4e3 35%,#35559a 65%,#4f7b36 100%)"></div>
  <div class="abs" style="left:85px;top:0;width:100px;height:145px;background:rgba(27,43,112,.85)"></div>
  <div class="abs" style="left:20px;top:18px;font-weight:700;font-size:10px;color:#fff">Lorem ipsum dolor</div>
  <div class="tx-w abs" style="left:90px;top:36px;width:88px">Lorem ipsum dolor sit amet, consectetur adipiscing elit, sed do eiusmod tempor incididunt ut labore et dolore magna aliqua. Lorem ipsum dolor sit amet, consectetur adipiscing elit sed do eiusmod tempor.<br><br>Lorem ipsum dolor sit amet, consectetur adipiscing elit, sed do eiusmod tempor incididunt ut labore et dolore magna aliqua sit amet.</div>
  <div class="tx abs" style="left:182px;top:36px;width:66px">Lorem ipsum dolor sit amet, consectetur adipiscing elit, sed do eiusmod tempor incididunt ut labore et dolore magna aliqua dolor sit amet.<br><br>Lorem ipsum dolor sit amet, consectetur adipiscing elit, sed do eiusmod tempor incididunt ut labore et dolore magna.</div>
  <svg class="wave"><use href="#wave"/></svg>
</section>

<!-- 15 Team -->
<section class="slide" style="left:530px;top:603px">
  <div class="brand"><i></i>NORVALE</div>
  <div class="title">YOUR TITLE GOES HERE</div>
  <div class="abs" style="left:0;top:38px;width:257px;height:34px;background:var(--green)"></div>
  <div class="abs" style="left:38px;top:30px;display:flex;gap:4px">
    <div style="width:44px"><div class="photo" role="img" aria-label="Portrait of team member" style="position:relative;width:44px;height:42px;background:linear-gradient(180deg,#8a8580,#3c3a3a)"></div><div class="hd" style="color:var(--navy);margin-top:3px">Lena Ortiz</div><div class="tx">Lorem Ipsum</div><div class="tx" style="margin-top:3px">Lorem ipsum dolor sit amet, consectetur adipiscing elit.</div></div>
    <div style="width:44px"><div class="photo" role="img" aria-label="Portrait of team member" style="position:relative;width:44px;height:42px;background:linear-gradient(180deg,#9a9a9a,#2f2f33)"></div><div class="hd" style="color:var(--navy);margin-top:3px">Marco Reyes</div><div class="tx">Lorem Ipsum</div><div class="tx" style="margin-top:3px">Lorem ipsum dolor sit amet, consectetur adipiscing elit.</div></div>
    <div style="width:44px"><div class="photo" role="img" aria-label="Portrait of team member" style="position:relative;width:44px;height:42px;background:linear-gradient(180deg,#b0b5b0,#4a4e4a)"></div><div class="hd" style="color:var(--navy);margin-top:3px">Davi Lima</div><div class="tx">Lorem Ipsum</div><div class="tx" style="margin-top:3px">Lorem ipsum dolor sit amet, consectetur adipiscing elit.</div></div>
    <div style="width:44px"><div class="photo" role="img" aria-label="Portrait of team member" style="position:relative;width:44px;height:42px;background:linear-gradient(180deg,#c9c4bd,#7c7066)"></div><div class="hd" style="color:var(--navy);margin-top:3px">Ana Souza</div><div class="tx">Lorem Ipsum</div><div class="tx" style="margin-top:3px">Lorem ipsum dolor sit amet, consectetur adipiscing elit.</div></div>
  </div>
  <svg class="wave"><use href="#wave"/></svg>
</section>

<!-- 16 Numbered table -->
<section class="slide" style="left:9px;top:752px">
  <div class="brand"><i></i>NORVALE</div>
  <div class="title">YOUR TITLE GOES HERE</div>
  <table class="abs" style="left:16px;top:30px;width:230px;font-size:2.5px;color:var(--text);text-align:center">
    <tr style="height:7px;color:#fff;font-weight:700"><td style="background:var(--gray);width:10px"></td><td style="background:var(--green)">Lorem ipsum dolor</td><td style="background:var(--navy)">Lorem ipsum dolor</td><td style="background:var(--green)">Lorem ipsum dolor</td><td style="background:var(--navy)">Lorem ipsum dolor</td></tr>
    <tr style="height:15px;background:#eee"><td>1</td><td>Lorem ipsum dolor sit consectetur adipiscing elit</td><td>Lorem ipsum dolor sit consectetur</td><td>25</td><td>348</td></tr>
    <tr style="height:15px"><td>2</td><td>Lorem ipsum dolor sit consectetur adipiscing elit</td><td>Lorem ipsum dolor sit consectetur</td><td>35</td><td>234</td></tr>
    <tr style="height:15px;background:#eee"><td>3</td><td>Lorem ipsum dolor sit consectetur adipiscing elit</td><td>Lorem ipsum dolor sit consectetur</td><td>65</td><td>235</td></tr>
    <tr style="height:15px"><td>4</td><td>Lorem ipsum dolor sit consectetur adipiscing elit</td><td>Lorem ipsum dolor sit consectetur</td><td>45</td><td>566</td></tr>
  </table>
  <div class="abs" style="left:18px;top:107px;display:flex;gap:16px">
    <div style="display:flex;gap:3px;width:64px"><span class="circ" style="flex:none;width:11px;height:11px;background:var(--navy)"></span><div class="tx"><b>Lorem ipsum dolor</b><br>Lorem ipsum dolor sit amet</div></div>
    <div style="display:flex;gap:3px;width:64px"><span class="circ" style="flex:none;width:11px;height:11px;background:var(--green)"></span><div class="tx"><b>Lorem ipsum dolor</b><br>Lorem ipsum dolor sit amet</div></div>
    <div style="display:flex;gap:3px;width:64px"><span class="circ" style="flex:none;width:11px;height:11px;background:var(--gray)"></span><div class="tx"><b>Lorem ipsum dolor</b><br>Lorem ipsum dolor sit amet</div></div>
  </div>
  <svg class="wave"><use href="#wave"/></svg>
</section>

<!-- 17 Org chart -->
<section class="slide" style="left:270px;top:752px">
  <div class="brand"><i></i>NORVALE</div>
  <div class="title" style="top:12px">YOUR TITLE GOES HERE</div>
  <svg class="abs" style="left:0;top:0" width="257" height="145" viewBox="0 0 257 145">
    <g stroke="#bbb" stroke-width=".6" fill="none">
      <path d="M128 38 V44 M52 44 H204 M52 44 V48 M128 44 V48 M204 44 V48"/>
      <path d="M32 60 V118 M32 66 H40 M32 88 H40 M32 110 H40"/>
      <path d="M108 60 V118 M108 66 H116 M108 88 H116 M108 110 H116"/>
      <path d="M184 60 V118 M184 66 H192 M184 88 H192 M184 110 H192"/>
    </g>
    <rect x="104" y="26" width="48" height="5" fill="#1b2b70"/><rect x="104" y="31" width="48" height="5" fill="#1fa21f"/>
    <g fill="#1fa21f"><rect x="28" y="48" width="48" height="5" fill="#1b2b70"/><rect x="28" y="53" width="48" height="5"/>
    <rect x="104" y="48" width="48" height="5" fill="#1b2b70"/><rect x="104" y="53" width="48" height="5"/>
    <rect x="180" y="48" width="48" height="5" fill="#1b2b70"/><rect x="180" y="53" width="48" height="5"/></g>
    <g fill="#ddd"><rect x="40" y="62" width="36" height="4"/><rect x="40" y="66" width="36" height="4" fill="#eee"/>
    <rect x="40" y="84" width="36" height="4"/><rect x="40" y="88" width="36" height="4" fill="#eee"/>
    <rect x="40" y="106" width="36" height="4"/><rect x="40" y="110" width="36" height="4" fill="#eee"/>
    <rect x="116" y="62" width="36" height="4"/><rect x="116" y="66" width="36" height="4" fill="#eee"/>
    <rect x="116" y="84" width="36" height="4"/><rect x="116" y="88" width="36" height="4" fill="#eee"/>
    <rect x="116" y="106" width="36" height="4"/><rect x="116" y="110" width="36" height="4" fill="#eee"/>
    <rect x="192" y="62" width="36" height="4"/><rect x="192" y="66" width="36" height="4" fill="#eee"/>
    <rect x="192" y="84" width="36" height="4"/><rect x="192" y="88" width="36" height="4" fill="#eee"/>
    <rect x="192" y="106" width="36" height="4"/><rect x="192" y="110" width="36" height="4" fill="#eee"/></g>
    <g font-size="2.4" fill="#fff" text-anchor="middle" font-family="Open Sans, sans-serif">
      <text x="128" y="29.8">FIRST / LAST NAME</text><text x="128" y="34.8">Position</text>
      <text x="52" y="51.8">FIRST / LAST NAME</text><text x="52" y="56.8">Position</text>
      <text x="128" y="51.8">FIRST / LAST NAME</text><text x="128" y="56.8">Position</text>
      <text x="204" y="51.8">FIRST / LAST NAME</text><text x="204" y="56.8">Position</text>
    </g>
    <g font-size="2.2" fill="#888" text-anchor="middle" font-family="Open Sans, sans-serif">
      <text x="58" y="65">FIRST / LAST NAME</text><text x="58" y="87">FIRST / LAST NAME</text><text x="58" y="109">FIRST / LAST NAME</text>
      <text x="134" y="65">FIRST / LAST NAME</text><text x="134" y="87">FIRST / LAST NAME</text><text x="134" y="109">FIRST / LAST NAME</text>
      <text x="210" y="65">FIRST / LAST NAME</text><text x="210" y="87">FIRST / LAST NAME</text><text x="210" y="109">FIRST / LAST NAME</text>
    </g>
  </svg>
  <svg class="wave"><use href="#wave"/></svg>
</section>

<!-- 18 Stats & charts -->
<section class="slide" style="left:530px;top:752px">
  <div class="brand"><i></i>NORVALE</div>
  <div class="title">YOUR TITLE GOES HERE</div>
  <div class="abs" style="left:16px;top:38px;font-weight:700;font-size:17px;color:var(--gray)">250K</div>
  <div class="abs" style="left:66px;top:37px;width:66px"><div class="hd" style="color:var(--navy);font-size:3px">Sed ut perspiciatis</div><div class="tx">Sed ut perspiciatis, unde omnis iste natus error sit voluptatem accusantium doloremque laudantium, totam rem.</div></div>
  <svg class="abs" style="left:16px;top:68px" width="120" height="40" viewBox="0 0 120 40">
    <g><rect x="2" y="2" width="100" height="2" fill="#1fa21f"/><rect x="2" y="5" width="85" height="2" fill="#1b2b70"/>
    <rect x="2" y="11" width="70" height="2" fill="#1fa21f"/><rect x="2" y="14" width="95" height="2" fill="#1b2b70"/>
    <rect x="2" y="20" width="88" height="2" fill="#1fa21f"/><rect x="2" y="23" width="60" height="2" fill="#1b2b70"/>
    <rect x="2" y="29" width="40" height="2" fill="#1fa21f"/><rect x="2" y="32" width="75" height="2" fill="#1b2b70"/></g>
    <line x1="2" y1="36" x2="118" y2="36" stroke="#999" stroke-width=".4"/>
    <g font-size="2.4" fill="#666" font-family="Open Sans, sans-serif"><text x="1" y="40">0</text><text x="15" y="40">1</text><text x="29" y="40">2</text><text x="43" y="40">3</text><text x="57" y="40">4</text><text x="71" y="40">5</text><text x="85" y="40">6</text><text x="99" y="40">7</text><text x="113" y="40">8</text></g>
  </svg>
  <svg class="abs" style="left:170px;top:50px" width="84" height="62" viewBox="0 0 84 62">
    <path d="M22 32 L22 10 A22 22 0 0 1 42 22Z" fill="#1b2b70"/>
    <path d="M22 32 L42 22 A22 22 0 0 1 12 52Z" fill="#1fa21f"/>
    <path d="M22 32 L12 52 A22 22 0 0 1 22 10Z" fill="#cfcfcf"/>
    <path d="M56 12 A18 18 0 1 1 44 44 L56 30Z" fill="#1b2b70"/>
    <g font-size="2.6" fill="#555" font-family="Open Sans, sans-serif"><text x="4" y="8">20%</text><text x="40" y="8">40%</text><text x="4" y="58">25%</text><text x="74" y="24">15%</text></g>
  </svg>
  <svg class="wave"><use href="#wave"/></svg>
</section>

<!-- 19 Cycle diagram -->
<section class="slide" style="left:9px;top:901px">
  <div class="brand"><i></i>NORVALE</div>
  <div class="title">YOUR TITLE GOES HERE</div>
  <svg class="abs" style="left:86px;top:32px" width="86" height="90" viewBox="0 0 86 90">
    <circle cx="43" cy="46" r="28" fill="none" stroke="#1fa21f" stroke-width="1.5"/>
    <circle cx="43" cy="46" r="12" fill="#1b2b70"/><circle cx="43" cy="46" r="8" fill="none" stroke="#fff" stroke-width="1.2"/><circle cx="43" cy="46" r="3" fill="#fff"/>
    <g fill="#1b2b70"><circle cx="29" cy="22" r="7"/><circle cx="71" cy="46" r="7"/><circle cx="29" cy="70" r="7"/></g>
    <g fill="#1fa21f"><circle cx="57" cy="22" r="7"/><circle cx="15" cy="46" r="7"/><circle cx="57" cy="70" r="7"/></g>
  </svg>
  <div class="tx abs" style="left:44px;top:36px;width:48px;text-align:right"><b>Add Text</b><br>Get a modern PowerPoint Presentation that is beautifully designed.</div>
  <div class="tx abs" style="left:26px;top:72px;width:48px;text-align:right"><b>Add Text</b><br>Get a modern PowerPoint Presentation that is beautifully designed.</div>
  <div class="tx abs" style="left:44px;top:108px;width:48px;text-align:right"><b>Add Text</b><br>Get a modern PowerPoint Presentation that is beautifully designed.</div>
  <div class="tx abs" style="left:166px;top:36px;width:48px"><b>Add Text</b><br>Get a modern PowerPoint Presentation that is beautifully designed.</div>
  <div class="tx abs" style="left:182px;top:72px;width:48px"><b>Add Text</b><br>Get a modern PowerPoint Presentation that is beautifully designed.</div>
  <div class="tx abs" style="left:166px;top:108px;width:48px"><b>Add Text</b><br>Get a modern PowerPoint Presentation that is beautifully designed.</div>
  <svg class="wave"><use href="#wave"/></svg>
</section>

<!-- 20 Timeline -->
<section class="slide" style="left:270px;top:901px">
  <div class="brand"><i></i>NORVALE</div>
  <div class="title">YOUR TITLE GOES HERE</div>
  <svg class="abs" style="left:0;top:54px" width="257" height="14" viewBox="0 0 257 14">
    <rect x="4" y="6.5" width="246" height="1.5" fill="#333"/><path d="M250 3 L256 7 L250 11Z" fill="#333"/>
    <path d="M36 1 H64 L58 13 H30Z" fill="#1fa21f"/>
    <path d="M84 1 H112 L106 13 H78Z" fill="#1b2b70"/>
    <path d="M132 1 H160 L154 13 H126Z" fill="#2456b8"/>
    <path d="M180 1 H208 L202 13 H174Z" fill="#f5c400"/>
    <path d="M228 1 H256 L250 13 H222Z" fill="#777"/>
    <g font-size="3" fill="#fff" text-anchor="middle" font-family="Open Sans, sans-serif" font-weight="700"><text x="47" y="8">2000</text><text x="95" y="8">2005</text><text x="143" y="8">2010</text><text x="191" y="8">2015</text><text x="239" y="8">2020</text></g>
  </svg>
  <div class="abs" style="left:20px;top:74px;display:flex;gap:8px;text-align:center">
    <div style="width:40px"><div class="hd" style="color:var(--green)">TITLE A</div><div class="tx">Lorem ipsum dolor sit amet, consectetur adipiscing elit.</div></div>
    <div style="width:40px"><div class="hd" style="color:var(--navy)">TITLE B</div><div class="tx">Lorem ipsum dolor sit amet, consectetur adipiscing elit.</div></div>
    <div style="width:40px"><div class="hd" style="color:var(--blue)">TITLE C</div><div class="tx">Lorem ipsum dolor sit amet, consectetur adipiscing elit.</div></div>
    <div style="width:40px"><div class="hd" style="color:#e0b400">TITLE D</div><div class="tx">Lorem ipsum dolor sit amet, consectetur adipiscing elit.</div></div>
    <div style="width:40px"><div class="hd" style="color:#666">TITLE E</div><div class="tx">Lorem ipsum dolor sit amet, consectetur adipiscing elit.</div></div>
  </div>
  <svg class="wave"><use href="#wave"/></svg>
</section>

<!-- 21 SWOT -->
<section class="slide" style="left:530px;top:901px">
  <div class="brand"><i></i>NORVALE</div>
  <svg class="abs" style="left:74px;top:16px" width="110" height="108" viewBox="0 0 110 108">
    <path d="M55 4 L74 23 L55 42 L36 23Z" fill="#1fa21f"/>
    <path d="M86 35 L105 54 L86 73 L67 54Z" fill="#2456b8"/>
    <path d="M55 66 L74 85 L55 104 L36 85Z" fill="#1b2b70"/>
    <path d="M24 35 L43 54 L24 73 L5 54Z" fill="#f5c400"/>
    <path d="M55 42 L67 54 L55 66 L43 54Z" fill="#1fa21f"/>
    <g font-family="Open Sans, sans-serif" font-weight="800" fill="#fff" text-anchor="middle">
      <text x="55" y="27" font-size="9">S</text><text x="86" y="58" font-size="9">W</text><text x="55" y="89" font-size="9">O</text><text x="24" y="58" font-size="9">T</text>
      <text x="55" y="56.5" font-size="6.5">SWOT</text>
    </g>
  </svg>
  <div class="abs" style="left:16px;top:34px;width:62px;text-align:right"><div class="hd" style="color:var(--green)">Strenghts</div><div class="tx">Lorem ipsum dolor sit amet, consectetuer adipiscing elit.</div></div>
  <div class="abs" style="left:16px;top:70px;width:62px;text-align:right"><div class="hd" style="color:#e0b400">Threats</div><div class="tx">Lorem ipsum dolor sit amet, consectetuer adipiscing elit.</div></div>
  <div class="abs" style="left:200px;top:54px;width:52px"><div class="hd" style="color:var(--navy)">Weaknesses</div><div class="tx">Lorem ipsum dolor sit amet, consectetuer adipiscing elit.</div></div>
  <div class="abs" style="left:200px;top:92px;width:52px"><div class="hd" style="color:var(--navy)">Opportunities</div><div class="tx">Lorem ipsum dolor sit amet, consectetuer adipiscing elit.</div></div>
  <svg class="wave"><use href="#wave"/></svg>
</section>

<!-- 22 Contact -->
<section class="slide" style="left:270px;top:1050px;background:#f4f4f4">
  <div class="photo" role="img" aria-label="Faint world map background" style="left:20px;top:10px;width:150px;height:90px;background:radial-gradient(ellipse,#e8e8e8 0%,#f4f4f4 70%)"></div>
  <svg class="abs" style="left:0;top:0" width="257" height="145" viewBox="0 0 257 145">
    <path d="M0 145 C110 140 200 110 257 30 L257 0 L257 145Z" fill="#fff" opacity=".0"/>
    <path d="M257 35 C220 95 150 135 40 145 L257 145Z" fill="#fff"/>
    <path d="M120 0 H257 V35 C240 30 200 20 120 0Z" fill="#8d8d8d"/>
    <rect x="120" y="0" width="137" height="40" fill="#8d8d8d"/>
  </svg>
  <div class="abs" style="left:140px;top:4px;font-weight:700;font-size:9px;color:#fff">Get in Touch</div>
  <div class="tx-w abs" style="left:136px;top:16px;width:110px">Lorem ipsum dolor sit amet, consectetur adipiscing elit sed do eiusmod tempor incididunt ut labore.</div>
  <div class="abs" style="left:14px;top:64px;font-weight:800;font-size:12px;color:var(--green)"><i style="display:inline-block;width:10px;height:10px;border-radius:50%;background:var(--green);margin-right:3px;vertical-align:-1px"></i>NORVALE Power</div>
  <div class="abs" style="left:140px;top:44px;display:flex;flex-direction:column;gap:9px">
    <div style="display:flex;gap:6px;align-items:center"><svg width="9" height="9" viewBox="0 0 10 10"><circle cx="5" cy="5" r="4.2" fill="none" stroke="#888" stroke-width=".8"/><path d="M1 5 H9 M5 1 C2 4 2 6 5 9 C8 6 8 4 5 1" fill="none" stroke="#888" stroke-width=".6"/></svg><span class="tx" style="color:#333">www.norvalepower.example</span></div>
    <div style="display:flex;gap:6px;align-items:center"><svg width="9" height="9" viewBox="0 0 10 10"><path d="M2 1 L4 1 L5 3.5 L3.8 4.5 C4.5 6 5 6.5 5.6 6.2 L6.5 5 L9 6 L9 8 C5 9.5 0.5 5 2 1Z" fill="#888"/></svg><span class="tx" style="color:#333">555.010.4420</span></div>
    <div style="display:flex;gap:6px;align-items:center"><svg width="9" height="9" viewBox="0 0 10 10"><rect x="1" y="2.5" width="8" height="5.5" fill="none" stroke="#888" stroke-width=".8"/><path d="M1 2.5 L5 6 L9 2.5" fill="none" stroke="#888" stroke-width=".8"/></svg><span class="tx" style="color:#333">info@norvalepower.example</span></div>
    <div style="display:flex;gap:6px;align-items:center"><svg width="9" height="9" viewBox="0 0 10 10"><path d="M5 9.5 C2 6 2 4.5 2 4 A3 3 0 0 1 8 4 C8 4.5 8 6 5 9.5Z" fill="none" stroke="#888" stroke-width=".8"/><circle cx="5" cy="4" r="1" fill="#888"/></svg><span class="tx" style="color:#333">Here to write your<br>Company adress</span></div>
  </div>
</section>

</body>
</html>
```